I need a business card design to compliment my existing branding [website and book give clear guidance here]. I teach business owners and managers how to become pioneers of business innovation in their industry - to challenge the paradigms and make their competition irrelevant. They will never look at business in the same way again.

The brand stands for innovation - to intelligently challenge the paradigms of each industry and seek to cause disruption. It's as provocative as it is progressive and many clients say that they find it quite uncomfortable to start with - they grow to love it and feel liberated by it.

The astronaut is the leading theme as it represents the pioneer, the maverick, the progressive ones. The astronaut can be as per the logo i.e. with the circle etc. or, can be extracted and used in isolation.

The word 'Masterclass' should not be used on the business card [even though it's in the attached logo].

Target Market(s)

Small to medium business owners, entrepreneurs, 'hungry' employees who want to accelerate their career

Industry/Entity Type

Business

Contact Information for Business Card

You. Pioneering Business Innovation.

Ned Farrow
Chief Innovation Coach

+61 [0]491 570 006
ned.farrow@coppermethodfinches.com
coppermethodfinches.com

Font styles to use
Other font styles liked:
• Eurostile

Requirements
Must have
• Simplistic and elegant is welcome.
• Colours and design must compliment the brand as per the attached documents - the book is probably the best guide as it is handed out at the same time as the business cards [whereas the website is looked at in isolation].
• I find the red stripe across the book cover quite striking.
• Font is Eurostile
Nice to have
• Unusual and eye catching but simple
Should not have
• No space scene in the background [i.e. it should not mimic the website banner]
• Other fonts than Eurostile

```html
<!DOCTYPE html>
<html lang="en">
<head>
<meta charset="utf-8">
<title>Copper Finches – Business Cards</title>
<link href="https://fonts.googleapis.com/css2?family=Michroma&family=Exo+2:wght@400;600&display=swap" rel="stylesheet">
<style>
  :root {
    --stage: #2b2b2d;
    --coral: #ef625e;
    --coral-soft: #f3786f;
    --navy: #1d3a4a;
    --paper: #ffffff;
    --ink: #27323a;
  }
  * { box-sizing: border-box; margin: 0; padding: 0; }
  html, body {
    width: 1200px; height: 917px; overflow: hidden;
    background: var(--stage);
  }
  .canvas { position: relative; width: 1200px; height: 917px; }

  .card {
    position: absolute;
    width: 560px; height: 320px;
    border-radius: 26px;
    overflow: hidden;
    box-shadow: 0 18px 40px rgba(0,0,0,.45);
  }

  /* Front */
  .card--front {
    left: 60px; top: 110px;
    background: var(--coral);
  }
  .card--front .backdrop {
    position: absolute; right: -60px; top: -80px;
    width: 340px; height: 340px; border-radius: 50%;
    background: radial-gradient(circle, var(--coral-soft) 0%, rgba(243,120,111,0) 70%);
  }
  .brand {
    position: absolute; left: 0; right: 0;
    display: flex; flex-direction: column; align-items: center; gap: 16px;
  }
  .card--front .brand { top: 92px; }
  .brand-dot { width: 74px; height: 74px; border-radius: 50%; }
  .card--front .brand-dot { background: var(--navy); }
  .brand-name {
    font-family: "Michroma", sans-serif;
    font-size: 26px; letter-spacing: 1px;
    text-transform: uppercase;
    white-space: nowrap;
  }
  .card--front .brand-name { color: var(--paper); }

  /* Back */
  .card--back {
    left: 580px; top: 480px;
    background: var(--paper);
  }
  .card--back .brand { top: 26px; gap: 12px; }
  .card--back .brand-dot { background: var(--navy); width: 70px; height: 70px; }
  .card--back .brand-name { color: var(--navy); font-size: 24px; }

  .name-band {
    position: absolute; left: 0; right: 0; top: 160px; height: 30px;
    background: var(--coral);
    display: flex; align-items: center; padding-left: 70px;
    font-family: "Michroma", sans-serif; color: var(--paper);
    white-space: nowrap;
  }
  .name-band .person { font-size: 15px; }
  .name-band .divider { margin: 0 10px; font-size: 15px; }
  .name-band .role { font-size: 11px; letter-spacing: .5px; }

  .contacts {
    position: absolute; left: 0; right: 0; top: 204px;
    font-family: "Exo 2", sans-serif; font-size: 14px; color: var(--ink);
  }
  .contact {
    position: absolute; display: flex; align-items: center; gap: 8px;
    white-space: nowrap;
  }
  .contact--phone { left: 56px; top: 26px; font-size: 15px; }
  .contact--email { left: 236px; top: 4px; }
  .contact--web { left: 236px; top: 34px; }
  .icon {
    width: 20px; height: 20px; border-radius: 50%;
    background: var(--coral);
    display: inline-flex; align-items: center; justify-content: center;
    flex: none;
  }
  .icon svg { width: 12px; height: 12px; }

  .base-band {
    position: absolute; left: 0; right: 0; top: 270px; height: 14px;
    background: var(--coral);
  }
</style>
</head>
<body>
<main class="canvas">

  <section class="card card--front" aria-label="Card front">
    <div class="backdrop" role="img" aria-label="Large faint astronaut illustration"></div>
    <div class="brand">
      <span class="brand-dot"></span>
      <span class="brand-name">Copper Finches</span>
    </div>
  </section>

  <section class="card card--back" aria-label="Card back">
    <div class="brand">
      <span class="brand-dot"></span>
      <span class="brand-name">Copper Finches</span>
    </div>

    <div class="name-band">
      <span class="person">NED FARROW</span>
      <span class="divider">/</span>
      <span class="role">CHIEF INNOVATION COACH</span>
    </div>

    <div class="contacts">
      <div class="contact contact--phone">
        <span class="icon">
          <svg viewBox="0 0 24 24"><path fill="#fff" d="M6.6 10.8a15.1 15.1 0 0 0 6.6 6.6l2.2-2.2a1 1 0 0 1 1-.25 11.4 11.4 0 0 0 3.6.57 1 1 0 0 1 1 1V20a1 1 0 0 1-1 1A17 17 0 0 1 3 4a1 1 0 0 1 1-1h3.5a1 1 0 0 1 1 1c0 1.25.2 2.45.57 3.57a1 1 0 0 1-.25 1z"/></svg>
        </span>
        +61 [0]491 570 006
      </div>
      <div class="contact contact--email">
        <span class="icon">
          <svg viewBox="0 0 24 24"><rect x="3" y="6" width="18" height="12" rx="1.5" fill="none" stroke="#fff" stroke-width="2"/><path d="M3.5 7l8.5 6 8.5-6" fill="none" stroke="#fff" stroke-width="2"/></svg>
        </span>
        ned.farrow@coppermethodfinches.com
      </div>
      <div class="contact contact--web">
        <span class="icon">
          <svg viewBox="0 0 24 24" fill="none" stroke="#fff" stroke-width="1.8"><circle cx="12" cy="12" r="9"/><ellipse cx="12" cy="12" rx="4" ry="9"/><path d="M3 12h18M5 7.5h14M5 16.5h14"/></svg>
        </span>
        coppermethodfinches.com
      </div>
    </div>

    <div class="base-band"></div>
  </section>

</main>
</body>
</html>
```